Pinmoor Services Website Design

We have most content but require a professional design. We have a logo already and will need it utilized along with several of the photos from the attached documentation.
First page should have our mission and Vision and the synapsis provided in the word document. Visitors will be prompted to select from one of our 3 divisions from this page.
Each division will have the same list of tabs : About, Services, Safety, Careers and Contact.
Photos on each divisions page should be representative of the divisions offerings. The word doc attached contains the requested content and we are open to edits that would complement and fill the website.
I like the Norquill site www.norquill.com - they are our competition so cant be modeled directly after this.
Please include prompts to request quote at each service page. align the format of the geotechnical page to the other 2 divisions.
I used chat gpt for some of the content so will need it optimized for SCO.

```html
<!DOCTYPE html>
<html lang="en">
<head>
<meta charset="utf-8">
<title>Pinmoor Services</title>
<link href="https://fonts.googleapis.com/css2?family=Unbounded:wght@600;800&family=Poppins:wght@400;500;600&display=swap" rel="stylesheet">
<style>
:root{
  --bg:#141414;
  --panel:#202020;
  --panel-2:#1a1a1a;
  --line:#2e2e2e;
  --red:#e5242a;
  --white:#ffffff;
  --muted:#a9a9a9;
  --head:"Unbounded",sans-serif;
  --body:"Poppins",sans-serif;
}
*{box-sizing:border-box;margin:0;padding:0}
html,body{width:1200px;height:3072px;overflow:hidden}
body{background:var(--bg);color:var(--white);font-family:var(--body);position:relative}
.abs{position:absolute}

/* nav */
.site-nav{left:0;top:0;width:1200px;height:64px;display:flex;align-items:center;justify-content:space-between;padding:0 16px 0 20px}
.brand{font-family:var(--head);font-weight:800;font-size:24px;color:var(--red);letter-spacing:1px}
.nav-links{display:flex;gap:4px;align-items:center}
.nav-links span{font-size:12px;font-weight:500;letter-spacing:.5px;padding:12px 14px;background:#222;color:var(--white)}
.nav-links .cta{background:var(--red)}

/* hero */
.hero{left:12px;top:64px;width:1176px;height:508px;background:linear-gradient(180deg,#5b6b4f 0%,#7c8a74 35%,#8d8c82 60%,#5a5750 100%)}
.hero::after{content:"";position:absolute;inset:0;background:linear-gradient(180deg,rgba(0,0,0,0) 40%,rgba(0,0,0,.55) 100%)}
.hero-copy{position:absolute;left:84px;top:290px;z-index:1}
.hero-copy h1{font-family:var(--head);font-weight:800;font-size:66px;letter-spacing:1px;line-height:1}
.hero-copy p{margin-top:26px;font-size:22px;line-height:1.4;max-width:640px}

/* cards */
.service-cards{left:12px;top:592px;width:1176px;height:208px;display:flex;gap:20px}
.card{flex:1;background:var(--panel);padding:34px 30px;position:relative}
.card h3{font-family:var(--head);font-weight:800;font-size:15px;letter-spacing:.5px}
.card p{margin-top:14px;font-size:14px;line-height:1.5;color:var(--muted);max-width:300px}
.more{position:absolute;left:30px;bottom:32px;display:flex;align-items:center;gap:14px;font-size:11px;font-weight:600;letter-spacing:1px}
.dot{width:26px;height:26px;border-radius:50%;background:#3a3a3a;display:flex;align-items:center;justify-content:center}

/* vision */
.vision-photo{left:12px;top:816px;width:580px;height:584px;background:linear-gradient(180deg,#8c98a3 0%,#a6adb0 35%,#7d7c76 55%,#56544f 100%)}
.vision-panel{left:608px;top:816px;width:580px;height:584px;background:var(--panel);display:flex;flex-direction:column;justify-content:center;align-items:center;text-align:center;padding:0 60px}
.section-title{font-family:var(--head);font-weight:800;font-size:38px;letter-spacing:1px}
.section-text{margin-top:24px;font-size:15px;line-height:1.6;color:var(--muted)}

/* mission */
.mission{left:12px;top:1416px;width:1176px;height:584px;background:var(--panel);display:flex;flex-direction:column;justify-content:center;align-items:center;text-align:center;padding:0 90px}

/* strip */
.aerial-strip{left:12px;top:2016px;width:1176px;height:208px;background:linear-gradient(180deg,#6e7a86 0%,#8a8f8a 40%,#6b6a63 70%,#4f4d48 100%)}

/* divisions */
.division-title{left:48px;top:2338px;font-family:var(--head);font-weight:800;font-size:34px;letter-spacing:1px}
.division{left:12px;width:1176px;height:104px;background:var(--panel);padding:24px 36px}
.division h4{font-family:var(--head);font-weight:600;font-size:13px;letter-spacing:.5px}
.division p{margin-top:14px;font-size:14px;color:var(--muted)}
.division .toggle{position:absolute;right:36px;top:36px;width:32px;height:32px;border-radius:50%;background:#3a3a3a;display:flex;align-items:center;justify-content:center}
.division.active{background:var(--red)}
.division.active p{color:#ffe3e3}
.division.active .toggle{background:var(--white)}

/* footer */
.footer{left:12px;top:2852px;width:1176px;height:128px;background:var(--panel-2);display:flex;padding:20px;gap:32px}
.footer-photo{width:340px;height:88px;background:linear-gradient(180deg,#7a8491,#6e6e68 60%,#4c4a46)}
.footer-col h5{font-family:var(--head);font-weight:800;font-size:14px;letter-spacing:.5px;margin-top:8px}
.footer-col p{margin-top:14px;font-size:12px;line-height:1.5}
.social{margin-left:auto;border-left:1px solid var(--line);padding-left:48px;width:190px}
.social-icons{display:flex;gap:12px;margin-top:18px}
.social-icons span{width:28px;height:28px;border-radius:50%;background:#333}
.bottom-bar{left:12px;top:2996px;width:1176px;height:60px;background:var(--panel-2);display:flex;justify-content:space-between;align-items:center;padding:0 24px;font-size:12px;color:var(--muted)}
.bottom-bar div{display:flex;gap:36px}
</style>
</head>
<body>

<header class="abs site-nav">
  <div class="brand">PINMOOR</div>
  <nav class="nav-links">
    <span>HOME</span><span>ABOUT</span><span>SERVICES</span><span>SAFETY</span><span>CAREERS &#9662;</span><span>CONTACT</span><span class="cta">GET IN TOUCH</span>
  </nav>
</header>

<section class="abs hero" role="img" aria-label="Aerial lift truck parked on a gravel lot in front of a forest">
  <div class="hero-copy">
    <h1>WHAT WE DO?</h1>
    <p>Delivering safe, reliable aerial access and maintenance services to Oil&amp;Gas,Construction, Utility, &amp; Renewable energy industries.</p>
  </div>
</section>

<section class="abs service-cards">
  <article class="card">
    <h3>AERIAL ACCESS</h3>
    <p>Full-servicewind energy service provider specializing in blade access and repair</p>
    <div class="more">VIEW MORE <span class="dot"><svg width="10" height="10" viewBox="0 0 10 10"><path d="M2 5h6M5 2l3 3-3 3" stroke="#fff" stroke-width="1.4" fill="none"/></svg></span></div>
  </article>
  <article class="card">
    <h3>GEOTECHNICAL DRILLING</h3>
    <p>Full-servicewind energy service provider specializing in blade access and repair</p>
    <div class="more">VIEW MORE <span class="dot"><svg width="10" height="10" viewBox="0 0 10 10"><path d="M2 5h6M5 2l3 3-3 3" stroke="#fff" stroke-width="1.4" fill="none"/></svg></span></div>
  </article>
  <article class="card">
    <h3>RENEWABLE ENERGY SERVICES</h3>
    <p>Full-servicewind energy service provider specializing in blade access and repair</p>
    <div class="more">VIEW MORE <span class="dot"><svg width="10" height="10" viewBox="0 0 10 10"><path d="M2 5h6M5 2l3 3-3 3" stroke="#fff" stroke-width="1.4" fill="none"/></svg></span></div>
  </article>
</section>

<div class="abs vision-photo" role="img" aria-label="Two aerial lift trucks parked on a gravel yard under an overcast sky"></div>
<section class="abs vision-panel">
  <h2 class="section-title">OUR VISION</h2>
  <p class="section-text">To be the leading provider of aerial access, geotechnical drilling, and service solutions, setting the standard for excellence in safety, efficiency, and environmental stewardship.</p>
</section>

<section class="abs mission">
  <h2 class="section-title">MISSION STATEMENT</h2>
  <p class="section-text">At Pinmoor, our mission is to deliver our specialized aerial access, geotechnical drilling, and service and maintenance solutions, consistently exceeding our clients' expectations. We strive to achieve this by investing in cutting-edge technology, fostering a culture of safety and continuous improvement, and prioritizing environmental stewardship. Through collaboration, integrity, and dedication, we aim to contribute to the success of our clients while maintaining the highest standards of quality and professionalism.</p>
</section>

<div class="abs aerial-strip" role="img" aria-label="Aerial view of the company yard and buildings in a small town"></div>

<h2 class="abs division-title">OUR DIVISION</h2>

<article class="abs division" style="top:2424px">
  <h4>AERIAL ACCESS</h4>
  <p>Full-servicewind energy service provider specializing in blade access and repair</p>
  <span class="toggle"><svg width="12" height="12" viewBox="0 0 12 12"><path d="M3 4.5l3 3 3-3" stroke="#fff" stroke-width="1.6" fill="none"/></svg></span>
</article>
<article class="abs division active" style="top:2560px;height:120px;padding-top:30px">
  <h4>GEOTECHNICAL DRILLING</h4>
  <p>Full-servicewind energy service provider specializing in blade access and repair</p>
  <span class="toggle" style="top:44px"><svg width="12" height="12" viewBox="0 0 12 12"><path d="M3 4.5l3 3 3-3" stroke="#e5242a" stroke-width="1.6" fill="none"/></svg></span>
</article>
<article class="abs division" style="top:2708px">
  <h4>RENEWABLE ENERGY SERVICES</h4>
  <p>Full-servicewind energy service provider specializing in blade access and repair</p>
  <span class="toggle"><svg width="12" height="12" viewBox="0 0 12 12"><path d="M3 4.5l3 3 3-3" stroke="#fff" stroke-width="1.6" fill="none"/></svg></span>
</article>

<footer class="abs footer">
  <div class="footer-photo" role="img" aria-label="Aerial view of the company yard"></div>
  <div class="footer-col" style="width:200px">
    <h5>ADDRESS</h5>
    <p>Elm Ridge, AB 210 Harbor Street T0M (587)555-0142</p>
  </div>
  <div class="footer-col" style="width:110px">
    <h5>PHONE</h5>
    <p>+1 587 555 0142</p>
  </div>
  <div class="footer-col">
    <h5>MAIL</h5>
    <p>info@pinmoorservices.com</p>
  </div>
  <div class="footer-col social">
    <h5>SOCIAL</h5>
    <div class="social-icons"><span></span><span></span><span></span></div>
  </div>
</footer>

<div class="abs bottom-bar">
  <span>&copy;Copyright 2024 Pinmoor | All rights reserved</span>
  <div><span>Privacy Policy</span><span>Cookie Policy</span></div>
</div>

</body>
</html>
```